依頼詳細
■選考方法
下記2点をPNGファイルでご提案ください。
※選定後に全てのパンフレットを作成いただきます。
※デザインを見たいので、中身のテキスト等はざっくりでかまいません。
①会社説明パンフの会社概要の部分(2P)のデザイン
②TideNote表紙と、中1P目のデザイン

■デザインの要望
・弊社ロゴ、製品ロゴを活かしたデザイン
・添付参考パンフレット、HP(http://www.kelvaro.co.jp/)をご参考下さい
・デザイン、色合いは統一

■納品物の形式
①aiデータ(印刷会社納品用)
②PNGデータ(弊社確認用)
※記載がない限りすべてサイズはA4、両面4色(CMYK)、左綴じです。

■納品物
※構成やテキストの草案はございます。
①会社説明 巻三つ折/6P
②MuvinSQ 見開き/4P
③BrimCaller 見開き/4P
④BrimNote 裏表/2P
⑤TideNote 裏表/2P
⑥BrimVPlayer 裏表/2P
⑦KoruRinger 裏表/2P
⑧QM437 裏表/2P※aiデータの文言、写真修正になります
⑨ポケットフォルダー 裏表/2P※外側のみのデザイン

サイズ
A4
ページ数
20ページ
希望イメージ
シンプル 複雑
単色 カラフル
暗い 明るい
日常 高級
遊び心 厳粛
未来的 伝統的
女性的 男性的
希望する色
青系、グレー系
納品ファイル
• イラストレーター形式 (.ai)
• PNG形式 (.png)
補足説明
■その他
・テキストはメイリオでお願いします。
・確認はしておりますが、誤字脱字がある場合修正頂けると助かります。
・段落の順番、テキスト内容以外は見栄えの良いようにして頂いて結構です。
・ロゴや、画像データはお渡しします。
・他で登録されているデザインや商標の転用など、他社の知的財産権、著作権を侵すことは禁止といたします。
・他のクライアントへ既に提案した内容の転用などもおやめ下さい。

■印刷
マットコート110kgで印刷予定です。

納品物の修正です
誤記× ⑤TideNote 裏表/2P
修正○ ⑤TideNote 見開き/4P
Excel、パワーポイントのPDF版を添付します。
■ 選んだ理由

コーポレートサイトとマッチしており、お客様に伝えたいことがわかりやすいため。

■ 提案者全員のお礼・コメント

様々なご提案を頂きましてありがとうございました。
また、決定までお時間を頂きまして誠に申し訳ございませんでした。

機会がございましたらよろしくお願いいたします。

```html
<!DOCTYPE html>
<html lang="ja">
<head>
<meta charset="utf-8">
<title>会社案内 表紙</title>
<link href="https://fonts.googleapis.com/css2?family=Noto+Sans+JP:wght@400;700&display=swap" rel="stylesheet">
<style>
  :root {
    --backdrop: #ffffff;
    --paper: #ffffff;
    --paper-edge: #d9dde2;
    --sky-light: #7fc3ee;
    --sky-mid: #2f8fd6;
    --sky-deep: #0d5ea8;
    --band-grey: #a9adb3;
    --band-orange: #d9572b;
    --band-green: #7fb239;
    --band-gold: #d7a51c;
    --ink: #5a5f66;
    --white: #ffffff;
  }
  * { margin: 0; padding: 0; box-sizing: border-box; }
  html, body {
    width: 825px; height: 1200px; overflow: hidden;
    background: var(--backdrop);
    font-family: "Noto Sans JP", sans-serif;
  }
  .cover {
    position: absolute; left: 38px; top: 70px;
    width: 746px; height: 1074px;
    background: var(--paper);
    border: 1px solid var(--paper-edge);
    box-shadow: 2px 3px 8px rgba(0,0,0,0.12);
    overflow: hidden;
  }
  .cover-visual {
    position: absolute; left: 0; top: 0; width: 100%; height: 818px;
    background:
      radial-gradient(ellipse 420px 380px at 42% 72%, rgba(255,255,255,0.45), transparent 70%),
      radial-gradient(ellipse 300px 500px at 85% 30%, rgba(190,230,255,0.5), transparent 70%),
      linear-gradient(160deg, var(--sky-light) 0%, var(--sky-mid) 45%, var(--sky-deep) 100%);
  }
  .title-strip {
    position: absolute; left: 0; top: 310px; width: 100%; height: 30px;
    display: flex; align-items: center;
  }
  .title-strip::after {
    content: ""; position: absolute; left: 0; right: 0; bottom: 0;
    height: 1px; background: rgba(255,255,255,0.55);
  }
  .cover-title {
    padding-left: 58px;
    color: var(--white); font-size: 17px; font-weight: 700;
    letter-spacing: 0.35em;
  }
  .accent-band {
    position: absolute; left: 0; top: 822px; width: 100%; height: 14px;
    display: flex; gap: 3px;
  }
  .accent-band span { height: 100%; }
  .band-grey { width: 182px; background: var(--band-grey); }
  .band-orange { width: 94px; background: var(--band-orange); }
  .band-green { width: 150px; background: var(--band-green); }
  .band-gold { flex: 1; background: var(--band-gold); }
  .brand {
    position: absolute; left: 44px; top: 940px;
    display: flex; align-items: center; gap: 12px;
  }
  .brand-mark { width: 22px; height: 22px; background: var(--band-gold); }
  .brand-name {
    color: var(--ink); font-size: 34px; font-weight: 400;
    letter-spacing: 0.12em;
  }
</style>
</head>
<body>
  <main class="cover">
    <div class="cover-visual" role="img" aria-label="青系の写真：地球儀、株価チャート、オフィスビルのガラス面を重ねたビジネスイメージ"></div>
    <div class="title-strip"><h1 class="cover-title">会社案内</h1></div>
    <div class="accent-band">
      <span class="band-grey"></span>
      <span class="band-orange"></span>
      <span class="band-green"></span>
      <span class="band-gold"></span>
    </div>
    <div class="brand">
      <span class="brand-mark"></span>
      <span class="brand-name">KELVARO</span>
    </div>
  </main>
</body>
</html>
```